Business card design for Tolbrin Waste

I would like double-sided business cards for myself and my partner that includes our logo and the existing colour scheme. We provide waste and environmental services to customers in the motor-vehicle and engineering industries.

```html
<!DOCTYPE html>
<html lang="en">
<head>
<meta charset="utf-8">
<title>Tolbrin Waste — Business Cards</title>
<link href="https://fonts.googleapis.com/css2?family=Montserrat:wght@600&family=Arimo:wght@400;700&display=swap" rel="stylesheet">
<style>
  :root {
    --stage: #2b2b2b;
    --card-dark: #434343;
    --card-dark-tone: #3d3f3b;
    --card-light: #ffffff;
    --green: #6aab34;
    --green-light: #8cc63f;
    --ink: #4a4a4a;
    --ink-soft: #5a5a5a;
    --rule: #9a9a9a;
  }
  * { box-sizing: border-box; margin: 0; padding: 0; }
  html, body { width: 1200px; height: 895px; overflow: hidden; }
  body {
    background: var(--stage);
    position: relative;
    font-family: "Arimo", Arial, sans-serif;
  }
  .card {
    position: absolute;
    width: 560px;
    height: 320px;
    border-radius: 2px;
    box-shadow: 0 12px 30px rgba(0,0,0,.45);
    overflow: hidden;
  }

  /* Front (dark) */
  .card--front {
    left: 80px; top: 110px;
    background: var(--card-dark);
  }
  .front__pattern {
    position: absolute; inset: 0;
    background: linear-gradient(135deg, var(--card-dark-tone), var(--card-dark));
  }
  .front__wordmark {
    position: absolute;
    left: 36px; bottom: 40px;
    font-family: "Montserrat", sans-serif;
    font-weight: 600;
    font-size: 30px;
    letter-spacing: 1px;
    color: #ffffff;
    line-height: 1;
  }

  /* Back (light) */
  .card--back {
    left: 560px; top: 465px;
    background: var(--card-light);
  }
  .brand {
    position: absolute;
    left: 0; right: 0; top: 72px;
    display: flex; align-items: center; justify-content: center;
    gap: 14px;
  }
  .brand__dot {
    width: 46px; height: 46px;
    border-radius: 50%;
    background: var(--green-light);
  }
  .brand__name {
    font-family: "Montserrat", sans-serif;
    font-weight: 600;
    font-size: 38px;
    letter-spacing: 1px;
    color: var(--ink);
    line-height: 1;
  }
  .contact {
    position: absolute;
    left: 0; right: 0; top: 190px;
    display: flex; justify-content: center; align-items: stretch;
    gap: 18px;
  }
  .person {
    text-align: right;
    color: var(--ink-soft);
    font-size: 13px;
    line-height: 1.3;
  }
  .person__name {
    color: var(--green);
    font-weight: 700;
    font-size: 19px;
    line-height: 1.2;
  }
  .divider {
    width: 1px;
    background: var(--rule);
  }
  .details {
    list-style: none;
    color: var(--ink-soft);
    font-size: 13px;
    line-height: 1.45;
  }
  .details li { display: flex; align-items: center; gap: 8px; }
  .details svg { width: 12px; height: 12px; fill: var(--green); flex: none; }
  .details .accent { color: var(--green); }
</style>
</head>
<body>

  <section class="card card--front">
    <div class="front__pattern" role="img" aria-label="Faint repeating leaf pattern in dark grey and olive tones"></div>
    <div class="front__wordmark">TOLBRIN WASTE</div>
  </section>

  <section class="card card--back">
    <div class="brand">
      <span class="brand__dot"></span>
      <span class="brand__name">TOLBRIN WASTE</span>
    </div>

    <div class="contact">
      <div class="person">
        <div class="person__name">Marlow Keaton</div>
        <div>Managing Partner</div>
        <div>142 NE Harbor Rd. Suite 9</div>
        <div>Lakeview, NY 97815</div>
      </div>
      <div class="divider"></div>
      <ul class="details">
        <li>
          <svg viewBox="0 0 24 24" aria-hidden="true"><path d="M6.6 10.8a15.1 15.1 0 0 0 6.6 6.6l2.2-2.2c.3-.3.7-.4 1-.2 1.1.4 2.3.6 3.6.6.6 0 1 .4 1 1V20c0 .6-.4 1-1 1A17 17 0 0 1 3 4c0-.6.4-1 1-1h3.5c.6 0 1 .4 1 1 0 1.3.2 2.5.6 3.6.1.3 0 .7-.2 1z"/></svg>
          000-000-0000
        </li>
        <li>
          <svg viewBox="0 0 24 24" aria-hidden="true"><path d="M6 3h12v5H6zM4 9h16a2 2 0 0 1 2 2v6h-4v4H6v-4H2v-6a2 2 0 0 1 2-2zm4 7v3h8v-3z"/></svg>
          999-999-9999
        </li>
        <li>
          <svg viewBox="0 0 24 24" aria-hidden="true"><path d="M2 5h20v14H2zm2 2v.5l8 5 8-5V7z"/></svg>
          <span>info@<span class="accent">tolbrinwaste</span>.com</span>
        </li>
        <li>
          <svg viewBox="0 0 24 24" aria-hidden="true"><path d="M12 2a10 10 0 1 0 0 20 10 10 0 0 0 0-20zm6.9 6h-3a15 15 0 0 0-1.3-4A8 8 0 0 1 18.9 8zM12 4c.8 1.2 1.5 2.5 1.9 4h-3.8c.4-1.5 1.1-2.8 1.9-4zM4.3 14a8 8 0 0 1 0-4h3.4a16 16 0 0 0 0 4zm.8 2h3a15 15 0 0 0 1.3 4A8 8 0 0 1 5.1 16zm3-8h-3a8 8 0 0 1 4.3-4A15 15 0 0 0 8.1 8zM12 20c-.8-1.2-1.5-2.5-1.9-4h3.8c-.4 1.5-1.1 2.8-1.9 4zm2.3-6H9.7a14 14 0 0 1 0-4h4.6a14 14 0 0 1 0 4zm.3 6a15 15 0 0 0 1.3-4h3a8 8 0 0 1-4.3 4zm1.7-6a16 16 0 0 0 0-4h3.4a8 8 0 0 1 0 4z"/></svg>
          <span>www.<span class="accent">tolbrinwaste</span>.com</span>
        </li>
      </ul>
    </div>
  </section>

</body>
</html>
```